New Business Card Design for Engineering and Surveying Company

We need a new design template for our business cards. We are a civil engineering, land surveying and pipeline integrity business. Please see dkhpartners.com for details. We need a bold, new business card design to complement our rebranding and marketing program. We have anew logo and attached vectro file. Please find additional details below. I am available to answer any questions.

Target Market(s)

Contractors, business owners, oil companies

Contact Information for Business Card

Needs to be customizable for different people (name, title, cell)

Font styles to use
Sans Serif
Other font styles liked:
• See eps file

Requirements
Must have
• Example Information:
Trevor Ashcombe

T:409-555-0173
M: 202-555-0148
tashcombe@dkhprtnrs.com

Address: 1875 Pinecrest Parkway, Beaumont, Texas 77703
Email: tolvanrey@dkhpartners.com
Website: www.dkhpartners.com
Nice to have
• I would like the back of the card to have the logo on a bold background with the text below:

[logo]
DORAN KESSLING & PARTNERS
CIVIL ENGINEERING | LAND SURVEYING | PIPELINE INTEGRITY

The reverse side should have the contact information for the person (example above), a smaller version of the logo and a graphic

```html
<!DOCTYPE html>
<html lang="en">
<head>
<meta charset="utf-8">
<title>DKH Business Card</title>
<link href="https://fonts.googleapis.com/css2?family=Work+Sans:wght@400;500;700;800&display=swap" rel="stylesheet">
<style>
  :root {
    --backdrop: #3b3b3d;
    --card: #1e1e1f;
    --white: #ffffff;
    --red: #e8202f;
    --blue: #2350a8;
    --muted: #d9d9d9;
  }
  * { box-sizing: border-box; margin: 0; padding: 0; }
  html, body {
    width: 1200px; height: 900px; overflow: hidden;
    background: var(--backdrop);
    font-family: "Work Sans", Arial, sans-serif;
  }
  .canvas {
    width: 1200px; height: 900px;
    display: flex; flex-direction: column; align-items: center; justify-content: center;
    gap: 30px;
  }
  .card {
    position: relative;
    width: 700px; height: 400px;
    background: var(--card);
    box-shadow: 0 10px 30px rgba(0,0,0,.45);
    color: var(--white);
  }
  .brand {
    display: flex; align-items: center; gap: 14px;
    font-weight: 800; color: var(--white); letter-spacing: 2px; line-height: 1;
  }
  .brand-dot { border-radius: 50%; background: var(--red); flex: none; }

  /* Back side */
  .card-back .identity {
    position: absolute; left: 120px; right: 60px; top: 110px;
    display: flex; flex-direction: column; align-items: center;
  }
  .card-back .brand { font-size: 96px; }
  .card-back .brand-dot { width: 36px; height: 36px; }
  .company-name {
    margin-top: 28px;
    color: var(--red); font-weight: 700; font-size: 20px; letter-spacing: 1.5px;
  }
  .services {
    margin-top: 10px;
    font-size: 15px; font-weight: 500; letter-spacing: 1.6px; color: var(--white);
  }

  /* Front side */
  .card-front .details { position: absolute; left: 54px; top: 48px; }
  .card-front .brand { font-size: 60px; }
  .card-front .brand-dot { width: 22px; height: 22px; }
  .person-name {
    margin-top: 18px;
    color: var(--red); font-weight: 700; font-size: 26px;
  }
  .address {
    margin-top: 16px; font-size: 16px; line-height: 1.35; color: var(--muted);
  }
  .contact-list { list-style: none; margin-top: 18px; }
  .contact-list li {
    display: flex; align-items: center; gap: 10px;
    font-size: 16px; line-height: 1.55; color: var(--muted);
  }
  .contact-list svg { width: 14px; height: 14px; fill: var(--blue); flex: none; }
</style>
</head>
<body>
<main class="canvas">

  <section class="card card-back" aria-label="Card back">
    <div class="identity">
      <div class="brand"><span class="brand-dot"></span>DKH</div>
      <p class="company-name">DORAN KESSLING &amp; PARTNERS</p>
      <p class="services">CIVIL ENGINEERING | LAND SURVEYING | PIPELINE INTEGRITY</p>
    </div>
  </section>

  <section class="card card-front" aria-label="Card front">
    <div class="details">
      <div class="brand"><span class="brand-dot"></span>DKH</div>
      <p class="person-name">Trevor Ashcombe</p>
      <p class="address">1875 Pinecrest Parkway<br>Beaumont, Texas 77703</p>
      <ul class="contact-list">
        <li>
          <svg viewBox="0 0 24 24" aria-hidden="true"><path d="M6.6 10.8a15.1 15.1 0 0 0 6.6 6.6l2.2-2.2c.3-.3.7-.4 1-.2 1.1.4 2.3.6 3.6.6.6 0 1 .4 1 1V20c0 .6-.4 1-1 1A17 17 0 0 1 3 4c0-.6.4-1 1-1h3.5c.6 0 1 .4 1 1 0 1.3.2 2.5.6 3.6.1.3 0 .7-.2 1l-2.3 2.2z"/></svg>
          409-555-0173
        </li>
        <li>
          <svg viewBox="0 0 24 24" aria-hidden="true"><path d="M7 1h10a2 2 0 0 1 2 2v18a2 2 0 0 1-2 2H7a2 2 0 0 1-2-2V3a2 2 0 0 1 2-2zm0 3v14h10V4H7zm5 15.5a1.2 1.2 0 1 0 0 2.4 1.2 1.2 0 0 0 0-2.4z"/></svg>
          202-555-0148
        </li>
        <li>
          <svg viewBox="0 0 24 24" aria-hidden="true"><path d="M2 5h20v14H2V5zm2 2v.5l8 5 8-5V7H4zm0 2.8V17h16V9.8l-8 5-8-5z"/></svg>
          tashcombe@dkhprtnrs.com
        </li>
        <li>
          <svg viewBox="0 0 24 24" aria-hidden="true"><path d="M12 2a10 10 0 1 0 0 20 10 10 0 0 0 0-20zm6.9 9h-3a15 15 0 0 0-1.3-6.1A8 8 0 0 1 18.9 11zM12 4c.9 1.2 1.8 3.6 1.9 7h-3.8c.1-3.4 1-5.8 1.9-7zM9.4 4.9A15 15 0 0 0 8.1 11h-3a8 8 0 0 1 4.3-6.1zM5.1 13h3a15 15 0 0 0 1.3 6.1A8 8 0 0 1 5.1 13zM12 20c-.9-1.2-1.8-3.6-1.9-7h3.8c-.1 3.4-1 5.8-1.9 7zm2.6-.9a15 15 0 0 0 1.3-6.1h3a8 8 0 0 1-4.3 6.1z"/></svg>
          www.dkhpartners.com
        </li>
      </ul>
    </div>
  </section>

</main>
</body>
</html>
```